Stationery Design Project for High End Wealth Management Firm

We need a stationery design for our high-end wealth management firm. Our clientele are affluent and our brand is built around providing investment services with world-class service.

The final concepts should provide a business card, letterhead, and envelope.

We like the idea of having text on the front and back and we MUST have black front and back business cards.
For the business card we have the following that needs to be included:
Company Logo & Tagline
Employee Name
Employee title
Employee Email
Website
2 seperate office cities, addresses, and phone numbers
Financial disclosure (small print)

Having black envelopes would be neat, but black is not a must for the envelopes.
Updates

Project Deadline Extended
Reason: To give the concept one more day of revisions.

Project Deadline Extended
Reason: To allow for more concepts and designs.

Target Market(s)

High Net Worth

Industry/Entity Type

Business

Requirements
Must have
• The following disclosure must be on the back of the card in small print:

Investment Advisory Services offered through Harrowgate Asset Partners LLC, a SEC Registered Investment Advisor. Corvane Wealth Management LLC is not affiliated with Harrowgate Asset Partners LLC.

Black business cards are also a must have.

Please utilize each of the 3 components of our logo in the design.

Please use our white background logo elements when designing our letterhead if you need them.
Nice to have
• Please use our company colors when designing. Utilize a combination of the elements of our logo that we have attached.

We are going to be printing our business cards on letterpress.

```html
<!DOCTYPE html>
<html lang="en">
<head>
<meta charset="utf-8">
<title>Corvane Wealth Management – Business Card</title>
<link rel="stylesheet" href="https://fonts.googleapis.com/css2?family=Arimo:wght@400;700&display=swap">
<style>
  :root {
    --backdrop: #3a3a3a;
    --card: #050505;
    --gold: #d9a24a;
    --gold-deep: #a8661f;
    --gold-light: #f3cf7e;
    --type-gold: #f0c54a;
    --white: #ffffff;
    --muted: #cfcfcf;
    --silver: #d8d8d8;
    --ink: #111111;
  }
  * { margin: 0; padding: 0; box-sizing: border-box; }
  html, body { width: 1200px; height: 534px; overflow: hidden; }
  body {
    background: var(--backdrop);
    font-family: "Arimo", Arial, sans-serif;
    position: relative;
  }
  .card {
    position: absolute;
    top: 117px;
    width: 525px;
    height: 300px;
    background: var(--card);
    border-radius: 22px;
    overflow: hidden;
  }
  .card--front { left: 62px; }
  .card--back { left: 620px; }

  /* front */
  .front-mark {
    position: absolute;
    left: 40px;
    top: 80px;
    width: 140px;
    height: 140px;
    border-radius: 50%;
    background: radial-gradient(circle at 35% 30%, var(--gold-light), var(--gold) 55%, var(--gold-deep));
  }
  .front-name {
    position: absolute;
    left: 210px;
    top: 179px;
    width: 296px;
    text-align: center;
    white-space: nowrap;
    color: var(--silver);
    font-size: 16px;
    letter-spacing: 0.5px;
    text-transform: uppercase;
  }
  .tagline {
    position: absolute;
    left: 210px;
    top: 229px;
    width: 296px;
    text-align: center;
    color: var(--white);
    font-size: 11px;
  }
  .disclosure {
    position: absolute;
    left: 222px;
    top: 253px;
    width: 272px;
    text-align: center;
    color: var(--muted);
    font-size: 5.6px;
    line-height: 1.55;
  }

  /* back */
  .back-brand {
    position: absolute;
    left: 36px;
    top: 50px;
    display: flex;
    align-items: center;
    gap: 10px;
  }
  .back-brand__dot {
    width: 34px;
    height: 34px;
    border-radius: 50%;
    background: radial-gradient(circle at 35% 30%, var(--gold-light), var(--gold) 55%, var(--gold-deep));
  }
  .back-brand__name {
    color: var(--silver);
    font-size: 17px;
    letter-spacing: 1px;
    text-transform: uppercase;
  }
  .contact {
    position: absolute;
    left: 37px;
    top: 146px;
    color: var(--white);
    font-size: 12.5px;
    line-height: 15px;
  }
  .contact__office-label { color: var(--type-gold); }
  .contact__phones { margin-top: 8px; }
  .contact__sep { color: #777; }
  .person {
    position: absolute;
    right: 30px;
    top: 146px;
    text-align: right;
  }
  .person__name {
    color: var(--type-gold);
    font-size: 17px;
    letter-spacing: 0.5px;
  }
  .person__title {
    color: var(--white);
    font-size: 12px;
    margin-top: 3px;
  }
  .gold-band {
    position: absolute;
    left: 0;
    right: 0;
    top: 226px;
    bottom: 0;
    background: linear-gradient(90deg, var(--gold-deep), var(--gold) 45%, var(--gold-light) 80%, #c98a35);
  }
  .website {
    position: absolute;
    right: 15px;
    top: 245px;
    color: var(--ink);
    font-size: 13px;
    letter-spacing: 1.5px;
  }
</style>
</head>
<body>

<section class="card card--front">
  <div class="front-mark"></div>
  <p class="front-name">Corvane Wealth Management</p>
  <p class="tagline">Preferred Wealth Management for Select Individuals</p>
  <p class="disclosure">
    Investment Advisory Services offered through Harrowgate Asset Partners LLC,<br>
    a SEC Registered Investment Advisor. Corvane Wealth Management LLC is not affiliated<br>
    with Harrowgate Asset Partners LLC.
  </p>
</section>

<section class="card card--back">
  <div class="back-brand">
    <span class="back-brand__dot"></span>
    <span class="back-brand__name">Corvane Wealth Management</span>
  </div>

  <div class="contact">
    <p><span class="contact__office-label">Office 1</span> office cities, addresses</p>
    <p><span class="contact__office-label">Office 1</span> office cities, addresses</p>
    <p class="contact__phones">p : 555 014 2280 <span class="contact__sep">|</span> 555 014 2280</p>
    <p>e : daniel.whitford@corvanewealth.com</p>
  </div>

  <div class="person">
    <p class="person__name">DANIEL WHITFORD</p>
    <p class="person__title">Position</p>
  </div>

  <div class="gold-band" role="img" aria-label="Decorative gold wave ornament along the bottom of the card"></div>

  <p class="website">www.corvanewealth.com</p>
</section>

</body>
</html>
```